Design of business signage for outside store front

We need signage designed for outside a store front.  We already have a logo, colours and font that we would like to use but would like some ideas as regards layout/design of the signage.  The final product will be for the use of the installer to produce and install the signage.  Attached are files with our logo and font and a picture of the current signage which needs to be replaced.  The size and shape of the signage will be the same as the current signage, its just the design/layout that we would like changed.
N.B. We would like two versions if possible, one with the web address and one without the web address to see what they look like.

```html
<!DOCTYPE html>
<html lang="en">
<head>
<meta charset="utf-8">
<title>Relish Iberia – Storefront Sign</title>
<link rel="stylesheet" href="https://fonts.googleapis.com/css2?family=Crimson+Pro:wght@600&family=Archivo:wght@400&family=Questrial&display=swap">
<style>
  :root {
    --page: #ffffff;
    --wine: #86232f;
    --wine-deep: #4a1119;
    --black: #000000;
    --gold: #f2d13a;
    --gold-soft: #b08f2c;
    --ink: #111111;
    --white: #ffffff;
  }
  html, body {
    margin: 0;
    width: 1200px;
    height: 690px;
    overflow: hidden;
    background: var(--page);
  }
  .sign {
    position: absolute;
    left: 84px;
    top: 122px;
    width: 1037px;
    height: 450px;
    background: linear-gradient(90deg, var(--wine) 0%, var(--wine) 12%, var(--wine-deep) 50%, var(--black) 100%);
    box-shadow: 6px 6px 6px rgba(0, 0, 0, 0.35);
    overflow: hidden;
  }
  .emblem-area {
    position: absolute;
    left: 59px;
    top: 26px;
    width: 278px;
    height: 409px;
    border-radius: 45% 45% 40% 40%;
    background: radial-gradient(ellipse at 55% 50%, rgba(255,255,255,0.55) 0%, rgba(242,209,58,0.55) 40%, rgba(176,143,44,0.25) 75%, rgba(176,143,44,0) 100%);
  }
  .sign-art {
    position: absolute;
    inset: 0;
    width: 100%;
    height: 100%;
  }
  .brand-name {
    font-family: "Crimson Pro", Georgia, serif;
    font-weight: 600;
    fill: var(--white);
  }
  .band { fill: url(#bandFade); }
  .tagline {
    font-family: "Archivo", Arial, sans-serif;
    font-size: 38px;
    fill: var(--ink);
  }
  .web-address {
    font-family: "Questrial", Arial, sans-serif;
    font-size: 40px;
    fill: var(--white);
  }
  .globe-icon { fill: none; stroke: var(--white); stroke-width: 2; }
</style>
</head>
<body>
  <div class="sign">
    <div class="emblem-area" role="img" aria-label="Brand emblem: gold ribbon swirl around a dancer figure"></div>
    <svg class="sign-art" viewBox="0 0 1037 450" xmlns="http://www.w3.org/2000/svg">
      <defs>
        <linearGradient id="bandFade" x1="0" y1="0" x2="1" y2="0">
          <stop offset="0" stop-color="#f2d13a"/>
          <stop offset="0.72" stop-color="#e6c537"/>
          <stop offset="0.9" stop-color="#a08a2a"/>
          <stop offset="1" stop-color="#1c1708"/>
        </linearGradient>
      </defs>

      <text class="brand-name" x="426" y="143" font-size="128" textLength="533" lengthAdjust="spacing">RELISH</text>
      <text class="brand-name" x="426" y="234" font-size="80" textLength="533" lengthAdjust="spacing">IBERIA</text>

      <path class="band" d="M353,288 Q380,317 359,346 L1037,346 L1037,288 Z"/>
      <text class="tagline" x="426" y="330" textLength="533" lengthAdjust="spacing">Spanish Artisan Foods</text>

      <g class="globe-icon">
        <circle cx="438" cy="398" r="12"/>
        <ellipse cx="438" cy="398" rx="5" ry="12"/>
        <line x1="426" y1="398" x2="450" y2="398"/>
        <line x1="428" y1="391" x2="448" y2="391"/>
        <line x1="428" y1="405" x2="448" y2="405"/>
        <line x1="438" y1="386" x2="438" y2="410"/>
      </g>
      <text class="web-address" x="466" y="410" textLength="493" lengthAdjust="spacing">www.relishiberia.com.au</text>
    </svg>
  </div>
</body>
</html>
```